Orvo kitchen designs

We are kitchen design company based in south Australia. We have high level of integrity and we believe strongly in what we do. Our aim is to put our clients in the driver seat, (it's your dream project not mine therefore your input is very important) which gives them control of their project, which we care about deeply.
We offer a detailed consultation, design package and or offer for a one of fee
to manage the project. We are also able to tender out the project to the local cabinet makers we work with. We are a service based company not a retail kitchen company. I like a matt black and a green which is what I gravitate to. The final design should convey integrity, quality with a strong belief in functional design.

Target Market(s)

both drawing for cabinet makers and the public more so the later

Contact Information for Business Card

logo with business name orvo kitchen design email liam.brennick@orvokitchendesigns.example and mobile number 0499 000 000
appointment details at back of card.

Logo Text

orvo kitchen designs with the use of (okd into the logo was my initial thought) open to your professional ideas.

Number of Pages Required

4 page

Font styles to use
Sans Serif
Other font styles liked:
• not sure a font to reflect info provided

Colors
9bcb3c

Requirements
Must have
• as above for business cards website page to flow through from that. Gallery pictures of kitchens etc. as with about us, contact page ' core home page. I need the easiest way to do a straight word press site with minimal plugins.
• I want what I have given you in the above info in project description to be on the website page, business cards and logo etc. I understand the logo is the core design element so this needs to he right. To have the proper colours & elements is also important.
Nice to have
• On website front page with logo in background perhaps. As i have mentioned in project description I want you to interpret that into of the project description so you can achieve the desired outcome.

```html
<!DOCTYPE html>
<html lang="en">
<head>
<meta charset="utf-8">
<title>Orvo Kitchen Designs</title>
<link href="https://fonts.googleapis.com/css2?family=Open+Sans:wght@400;600;700&display=swap" rel="stylesheet">
<style>
:root{
  --green:#2f5d3a;
  --green-dark:#264d30;
  --ink:#222222;
  --text:#555555;
  --soft:#f4f3f1;
  --charcoal:#333333;
  --white:#ffffff;
  --line:#e2e2e2;
}
*{box-sizing:border-box;margin:0;padding:0}
html,body{width:726px;height:1200px;overflow:hidden;background:var(--white)}
body{position:relative;font-family:'Open Sans',Arial,sans-serif;color:var(--text)}
.abs{position:absolute}
.top-band{left:0;top:0;width:726px;height:4px;background:var(--green)}

.brand{left:0;top:24px;width:726px;display:flex;justify-content:center;align-items:center;gap:8px}
.brand-square{width:30px;height:30px;border:3px solid var(--green)}
.brand-name{font-size:21px;font-weight:400;color:var(--green);letter-spacing:1px}

.nav{left:158px;top:80px;width:408px;border-top:1px solid var(--line);display:flex;justify-content:space-between;padding-top:9px;font-size:8.5px;color:#444}
.nav a{color:inherit;text-decoration:none;position:relative}
.nav a.active{color:var(--green)}
.nav a.active::before{content:"";position:absolute;left:-4px;right:-4px;top:-10px;height:2px;background:var(--green)}

.hero{left:67px;top:117px;width:592px;height:252px;background:linear-gradient(180deg,#a9a196 0%,#8a8276 45%,#6b4a36 100%)}
.hero-frame{left:6px;top:6px;right:6px;bottom:6px;border:1px solid rgba(255,255,255,.6)}
.hero-title{left:0;top:85px;width:100%;text-align:center;font-size:26px;font-weight:300;color:var(--white)}
.hero-title b{font-weight:700}
.hero-rule{left:255px;top:128px;width:78px;height:2px;background:var(--white)}
.hero-copy{left:140px;top:145px;width:312px;text-align:center;font-size:7px;line-height:11.5px;color:var(--white)}
.dots{left:0;top:180px;width:100%;display:flex;justify-content:center;gap:6px}
.dots span{width:5px;height:5px;border-radius:50%;border:1px solid var(--white)}
.dots span.on{background:var(--white)}

.about{left:67px;top:390px;width:592px;height:81px;background:var(--soft);text-align:center}
.section-title{font-size:16px;font-weight:600;color:var(--ink);letter-spacing:.3px}
.about .section-title{margin-top:14px}
.title-rule{width:32px;height:2px;background:var(--green);margin:4px auto 0}
.about p{font-size:7px;line-height:11.5px;width:400px;margin:7px auto 0}

.card{top:494px;width:170px;height:284px;border:1px solid var(--line);background:var(--white)}
.card-photo{left:0;top:0;width:168px;height:245px}
.photo-a{background:linear-gradient(180deg,#e4e1dc 0%,#cfcac2 55%,#6b4530 100%)}
.photo-b{background:linear-gradient(180deg,#c9c3b6 0%,#ddd3bd 60%,#b9a88a 100%)}
.photo-c{background:linear-gradient(180deg,#e9e4dc 0%,#d8d2c8 60%,#6a4634 100%)}
.tag-new{left:0;top:0;width:30px;height:18px;background:#2b2b2b;color:var(--white);font-size:8px;font-weight:700;text-align:center;line-height:18px}
.quick-view{left:49px;top:198px;width:80px;height:26px;border-radius:13px;background:#2b2b2b;border:2px solid var(--white);color:var(--white);font-size:8.5px;font-weight:600;text-align:center;line-height:22px;letter-spacing:.3px;box-shadow:0 0 0 1px #2b2b2b}
.card-meta{left:14px;right:14px;top:261px;display:flex;justify-content:space-between;font-size:7.5px}
.price{color:var(--green);font-weight:700}

.testimonials{left:66px;top:800px;width:592px;height:187px;background:var(--green);color:var(--white)}
.testimonials .section-title{position:absolute;left:45px;top:24px;color:var(--white);font-size:15px}
.testimonials .rule{left:45px;top:46px;width:32px;height:2px;background:var(--white)}
.quote-mark{font-size:62px;font-weight:700;line-height:1;color:var(--white)}
.quote-open{left:43px;top:58px}
.quote-close{left:521px;top:58px}
.testimonial-text{left:101px;top:72px;width:392px;font-size:7px;line-height:11.5px}
.avatar{left:45px;top:120px;width:40px;height:40px;border-radius:50%;border:2px solid var(--white);background:linear-gradient(180deg,#c9b39a,#8e7460)}
.client{left:102px;top:128px;font-size:7.5px;line-height:10px}
.client b{font-weight:600}
.arrow{top:131px;width:20px;height:20px;border-radius:50%;background:var(--white);border:2px solid #ccc}
.arrow svg{position:absolute;left:5px;top:5px}

.footer{left:68px;top:1008px;width:590px;height:159px;background:var(--charcoal);color:var(--white)}
.footer h3{position:absolute;top:22px;font-size:12px;font-weight:600}
.link-btn{height:13px;background:var(--green);font-size:6.5px;text-align:center;line-height:13px;color:var(--white)}
.foot-brand{left:20px;top:102px;display:flex;align-items:center;gap:6px}
.foot-brand .brand-square{width:24px;height:24px;border-color:var(--white);border-width:2px}
.foot-brand .brand-name{color:var(--white);font-size:14px}
.post{left:239px;width:190px;height:36px}
.post-thumb{left:0;top:0;width:38px;height:35px;background:linear-gradient(180deg,#d9d4cb,#9c8e7c)}
.post-text{left:50px;top:0;font-size:6.8px;line-height:11px;width:136px}
.post-meta{left:50px;top:26px;display:flex;gap:15px;font-size:6.5px;align-items:center}
.post-meta span{display:flex;align-items:center;gap:4px}
.address{left:456px;top:50px;font-size:6.8px;line-height:11.5px}
.addr-row{display:flex;gap:5px}
.addr-row svg{flex:none;margin-top:1px}
.copyright{left:456px;top:134px;font-size:6.8px;line-height:10px}
</style>
</head>
<body>
<div class="abs top-band"></div>

<header>
  <div class="abs brand">
    <span class="brand-square"></span>
    <span class="brand-name">orvo kitchen designs</span>
  </div>
  <nav class="abs nav">
    <a class="active" href="#">Home</a><a href="#">About Us</a><a href="#">Gallery</a><a href="#">Cabinets</a><a href="#">Design Service</a><a href="#">Blog</a><a href="#">Contact us</a>
  </nav>
</header>

<section class="abs hero" role="img" aria-label="Bright kitchen with white cabinets, stainless range and wooden floor">
  <div class="abs hero-frame"></div>
  <h1 class="abs hero-title">pre <b>assembled</b> cabinets</h1>
  <div class="abs hero-rule"></div>
  <p class="abs hero-copy">Lorem ipsum dolor sit amet, consectetur adipiscing elit. Tuo vero id quidem, inquam, arbitratu. Nemo nostrum istius generis asotos iucunde putat vivere.</p>
  <div class="abs dots"><span class="on"></span><span></span><span></span></div>
</section>

<section class="abs about">
  <h2 class="section-title">ABOUT US</h2>
  <div class="title-rule"></div>
  <p>Lorem ipsum dolor sit amet, consectetur adipiscing elit. Tuo vero id quidem, inquam, arbitratu. Nemo nostrum istius generis asotos iucunde putat vivere. Nulla profecto est, quin suam vim retineat a primo ad extremum.</p>
</section>

<article class="abs card" style="left:68px">
  <div class="abs card-photo photo-a" role="img" aria-label="White shaker kitchen with dark island and timber floor"></div>
  <div class="abs tag-new">NEW</div>
  <div class="abs quick-view">QUICK VIEW</div>
  <div class="abs card-meta"><span>New Arrivals</span><span class="price">$750.00</span></div>
</article>
<article class="abs card" style="left:278px">
  <div class="abs card-photo photo-b" role="img" aria-label="Cream kitchen with window, plants and dark benchtop"></div>
  <div class="abs tag-new">NEW</div>
  <div class="abs quick-view">QUICK VIEW</div>
  <div class="abs card-meta"><span>Sample Kitchen</span><span class="price">$750.00</span></div>
</article>
<article class="abs card" style="left:489px">
  <div class="abs card-photo photo-c" role="img" aria-label="White kitchen cabinets under a window with dishwasher"></div>
  <div class="abs tag-new">NEW</div>
  <div class="abs quick-view">QUICK VIEW</div>
  <div class="abs card-meta"><span>Cabnets</span><span class="price">$750.00</span></div>
</article>

<section class="abs testimonials">
  <h2 class="section-title">TESTIMONIALS</h2>
  <div class="abs rule"></div>
  <div class="abs quote-mark quote-open">&ldquo;</div>
  <div class="abs quote-mark quote-close">&rdquo;</div>
  <p class="abs testimonial-text">Lorem ipsum dolor sit amet, consectetur adipiscing elit. Tuo vero id quidem, inquam, arbitratu. Nemo nostrum istius generis asotos iucunde putat vivere. Nulla profecto est, quin suam vim retineat a primo ad extremum. Prioris generis est docilitas, memoria; Minime vero, inquit ille, consentit. Cur tantas regiones barbarorum pedibus obiit, tot maria transmisit? Sed quanta sit alias, nunc tantum possitne esse tanta.</p>
  <div class="abs avatar" role="img" aria-label="Client portrait"></div>
  <div class="abs client"><b>Client Name</b><br>Designation</div>
  <div class="abs arrow" style="left:506px"><svg width="8" height="8" viewBox="0 0 8 8"><path d="M5.5 1 2.5 4l3 3" fill="none" stroke="#222" stroke-width="1.3"/></svg></div>
  <div class="abs arrow" style="left:530px"><svg width="8" height="8" viewBox="0 0 8 8"><path d="M2.5 1l3 3-3 3" fill="none" stroke="#222" stroke-width="1.3"/></svg></div>
</section>

<footer class="abs footer">
  <h3 style="left:20px">LINKS</h3>
  <div class="abs link-btn" style="left:23px;top:55px;width:78px">Home</div>
  <div class="abs link-btn" style="left:104px;top:55px;width:66px">About Us</div>
  <div class="abs link-btn" style="left:173px;top:55px;width:90px">Cabinets</div>
  <div class="abs link-btn" style="left:23px;top:72px;width:76px">Service</div>
  <div class="abs link-btn" style="left:102px;top:72px;width:44px">Blog</div>
  <div class="abs link-btn" style="left:149px;top:72px;width:73px">Contact Us</div>
  <div class="abs foot-brand"><span class="brand-square"></span><span class="brand-name">orvo kitchen designs</span></div>

  <h3 style="left:239px">LASEST POSTS</h3>
  <div class="abs post" style="top:50px">
    <div class="abs post-thumb" role="img" aria-label="Kitchen with flowers on the bench"></div>
    <p class="abs post-text">Lorem ipsum dolor sit amet, consectetur adipiscing elit. Tuo vero id quidem,</p>
    <div class="abs post-meta">
      <span><svg width="10" height="9" viewBox="0 0 10 9"><path d="M0 4.5 4.5 0H10v5.5L5.5 9z" fill="#fff"/><circle cx="7.5" cy="2" r=".9" fill="#333"/></svg>Likes</span>
      <span><svg width="10" height="9" viewBox="0 0 10 9"><path d="M0 0h10v6.5H4L1.5 9V6.5H0z" fill="#fff"/></svg>6 Comments</span>
    </div>
  </div>
  <div class="abs post" style="top:101px">
    <div class="abs post-thumb" role="img" aria-label="Kitchen range with cabinets"></div>
    <p class="abs post-text">Lorem ipsum dolor sit amet, consectetur adipiscing elit. Tuo vero id quidem,</p>
    <div class="abs post-meta">
      <span><svg width="10" height="9" viewBox="0 0 10 9"><path d="M0 4.5 4.5 0H10v5.5L5.5 9z" fill="#fff"/><circle cx="7.5" cy="2" r=".9" fill="#333"/></svg>Likes</span>
      <span><svg width="10" height="9" viewBox="0 0 10 9"><path d="M0 0h10v6.5H4L1.5 9V6.5H0z" fill="#fff"/></svg>6 Comments</span>
    </div>
  </div>

  <h3 style="left:456px">ADDRESS</h3>
  <div class="abs address">
    <div class="addr-row"><svg width="8" height="10" viewBox="0 0 8 10"><path d="M4 0a4 4 0 0 1 4 4c0 3-4 6-4 6S0 7 0 4a4 4 0 0 1 4-4z" fill="#fff"/><circle cx="4" cy="4" r="1.4" fill="#333"/></svg><span>Sample Location is Here<br>P. O. Box 1234<br>Company Name, AB 12345</span></div>
    <div class="addr-row" style="margin-top:6px"><svg width="9" height="7" viewBox="0 0 9 7"><rect x=".5" y=".5" width="8" height="6" fill="none" stroke="#fff"/><path d="M.5.5 4.5 4l4-3.5" fill="none" stroke="#fff"/></svg><span>info@orvomail.example<br>www.orvokitchendesigns.example</span></div>
  </div>
  <div class="abs copyright">&copy; 2017 Orvo Kitchen Designs</div>
</footer>
</body>
</html>
```